Office brochure for chronic pain doctor

I need an brochure for my office, and since I want to be able to mail the brochure, I think trifold would be the best size. I treat patients with chronic head and neck pain, as well as sleep apnea. I treat all of the following:

1. headaches
2. myofascial pain, which is a fancy way of saying muscle pain
3. neuropathic pain, which is a fancy way of saying nerve pain
4. TMJ, which stands for the temporomandibular joint (jaw joint)
5. obstructive sleep apnea

The colors will be based on my logo on my website, which you can see at www.BrightJPR.net, and you can learn more about what I do at my website. JPR stands for orofacial pain, which is a speciality training within the field of dentistry but I do not treat teeth. I have high resolution graphics for the brochure so I need someone with an artistic eye to design and lay out the brochure.

The logo colors are:
Purple 9e80bb
Pink f6b1d0
Blue 0f4b8f
Updates

I had a request for the logo in a .ai or .pdf format, which I have just uploaded. Please let me know if you have any other requests. Thank you, Dale

Target Market(s)

80% female, 20% male. I am in an upscale area of Los Angeles called Beverly Hills but I will see a patient from any area around Los Angeles or from any area in the world.

Industry/Entity Type

Training

Colors
6b449b
e567a6
0355a3

Requirements
Must have
• I want a small section of the brochure to feature each of the five areas I treat, and I have included an image to place in each of the five sections. A small section should include a short bio of me, which you can condense from www.brightjpr.net/dale. The brochure must appeal to women since 80% of my patients are female but I don't want to completely ignore men. Most of the pain patients are female, and most of the sleep apnea patients are male.

Here are the colors in my logo
Purple 9e80bb
Pink f6b1d0
Blue 0f4b8f
Should not have
• Anything related to teeth or dentistry.
No decorative or script fonts.

```html
<!DOCTYPE html>
<html lang="en">
<head>
<meta charset="utf-8">
<title>Bright JPR Trifold Brochure</title>
<link href="https://fonts.googleapis.com/css2?family=Arimo:wght@400;700&display=swap" rel="stylesheet">
<style>
  :root {
    --page-bg: #e4e4e4;
    --purple: #9b80bb;
    --purple-text: #a98fcc;
    --navy: #1a1c3a;
    --blue: #1f4e92;
    --blue-light: #6d9ad3;
    --pink: #f2a9cb;
    --white: #ffffff;
    --photo-top: #6f7f7c;
    --photo-bottom: #46544f;
  }
  * { margin: 0; padding: 0; box-sizing: border-box; }
  html, body { width: 1200px; height: 1000px; overflow: hidden; }
  body { background: var(--page-bg); font-family: "Arimo", Arial, sans-serif; position: relative; }

  .brochure {
    position: absolute; left: 152px; top: 141px; width: 890px; height: 690px;
    display: flex; box-shadow: 0 6px 24px rgba(0,0,0,.35);
  }
  .panel { position: relative; height: 100%; }
  .panel--intro { width: 294px; background: var(--purple); }
  .panel--bio { width: 295px; background: var(--navy); }
  .panel--cover { width: 301px; background: var(--navy); }

  /* Intro panel */
  .intro__kicker { position: absolute; left: 17px; top: 32px; color: var(--white); font-weight: 700; font-size: 15px; letter-spacing: .3px; }
  .intro__title { position: absolute; left: 16px; top: 53px; color: var(--blue); font-weight: 700; font-size: 28.5px; letter-spacing: .3px; }
  .intro__body {
    position: absolute; left: 15px; top: 106px; width: 271px;
    color: var(--white); font-size: 15px; line-height: 18.6px; text-align: justify; hyphens: auto;
  }
  .conditions { position: absolute; left: 15px; top: 589px; width: 269px; height: 85px; display: flex; gap: 1px; }
  .condition { flex: 1; display: flex; flex-direction: column; }
  .condition__image { flex: 1; background: linear-gradient(#d9d9d9, #8a8a8a); }
  .condition__label {
    height: 11px; background: var(--blue-light); color: var(--white);
    font-size: 7px; line-height: 11px; text-align: center;
  }
  .condition--dark .condition__label { background: var(--blue); }

  /* Bio panel */
  .bio__portrait { position: absolute; left: 1px; top: 1px; width: 294px; height: 299px; background: linear-gradient(var(--photo-top), var(--photo-bottom)); }
  .bio__name { position: absolute; left: 0; top: 318px; width: 100%; text-align: center; color: var(--white); font-size: 26px; letter-spacing: .5px; }
  .bio__degrees { position: absolute; left: 0; top: 347px; width: 100%; text-align: center; color: var(--purple-text); font-size: 14px; letter-spacing: .5px; }
  .bio__text {
    position: absolute; left: 15px; top: 377px; width: 271px;
    color: var(--white); font-size: 12.3px; line-height: 15.6px; text-align: justify;
  }
  .bio__board { position: absolute; left: 0; top: 529px; width: 100%; text-align: center; color: var(--white); font-size: 19px; line-height: 24px; }
  .bio__address { position: absolute; left: 0; top: 583px; width: 100%; text-align: center; color: var(--purple-text); font-size: 15px; line-height: 19px; letter-spacing: .6px; }
  .bio__phone { position: absolute; left: 0; top: 625px; width: 100%; text-align: center; color: var(--purple-text); font-size: 15px; letter-spacing: .6px; }
  .bio__web { position: absolute; left: 0; top: 655px; width: 100%; text-align: center; color: var(--pink); font-size: 20px; letter-spacing: 1px; }

  /* Cover panel */
  .brand { position: absolute; left: 0; top: 160px; width: 100%; display: flex; justify-content: center; align-items: center; gap: 12px; }
  .brand__mark { width: 40px; height: 40px; background: var(--pink); }
  .brand__name { color: var(--white); font-weight: 700; font-size: 26px; letter-spacing: 1px; }
  .cover__headline {
    position: absolute; left: 0; top: 240px; width: 100%; text-align: center;
    color: var(--white); font-weight: 700; font-size: 24px; line-height: 30.5px; letter-spacing: 1.2px;
  }
  .testimonial__quote {
    position: absolute; left: 15px; top: 520px; width: 270px;
    color: var(--purple-text); font-size: 14.6px; line-height: 18.6px; text-align: justify;
  }
  .testimonial__author { position: absolute; right: 16px; top: 657px; color: var(--pink); font-size: 13px; }
</style>
</head>
<body>
  <main class="brochure">
    <section class="panel panel--intro">
      <p class="intro__kicker">Learn About</p>
      <h2 class="intro__title">Orofacial Pain</h2>
      <p class="intro__body">Orofacial pain, known as JPR for short, is the management of chronic head and neck pain using conservative treatment. A group of dentists at the Westbrook University School of Dentistry in the 1990's started to fill a niche treating patients who had undiagnosed chronic pain in the head and neck including headaches such as migraine, and cluster headaches, head and neck muscle pain, various nerve pains from sharp, shooting electrical pain to dull, aching, burning pain, TMJ, and obstructive sleep apnea. Although there is no specialty in TMJ treatment, the JPR residency at Westbrook is one of the few programs in the country that is recognized by the National Council on Clinical Accreditation or NCCA for short. Please read more about JPR orofacial pain by clicking on one of the various links above.</p>
      <div class="conditions">
        <div class="condition condition--dark"><div class="condition__image" role="img" aria-label="Black and white photo of a woman with a headache"></div><span class="condition__label">Headache</span></div>
        <div class="condition condition--dark"><div class="condition__image" role="img" aria-label="Black and white photo of a woman with neck muscle pain"></div><span class="condition__label">Muscle Pain</span></div>
        <div class="condition"><div class="condition__image" role="img" aria-label="Black and white photo of an older man with nerve pain"></div><span class="condition__label">Nerve Pain</span></div>
        <div class="condition"><div class="condition__image" role="img" aria-label="Black and white photo of a man sleeping"></div><span class="condition__label">Sleep Apnea</span></div>
        <div class="condition"><div class="condition__image" role="img" aria-label="Black and white photo of a woman with jaw pain"></div><span class="condition__label">TMJ</span></div>
      </div>
    </section>

    <section class="panel panel--bio">
      <div class="bio__portrait" role="img" aria-label="Portrait of the doctor in a white coat against a grey-green backdrop"></div>
      <h1 class="bio__name">Dale Whitcombe</h1>
      <p class="bio__degrees">DDS, MBA</p>
      <p class="bio__text">Dr. Dale Whitcombe is a dentist who does not treat teeth. Yes, you read that correctly. He completed a residency in orofacial pain and dental sleep medicine at Westbrook, and he does not believe that chronic head and neck pain is related to your bite, or what dentists call occlusion.</p>
      <p class="bio__board">Diplomate National Board of<br>Orofacial Pain</p>
      <p class="bio__address">4280 Marlow Avenue, Suite 210<br>Beverly Hills, CA 90210</p>
      <p class="bio__phone">555.014.2290</p>
      <p class="bio__web">www.BrightJPR.net</p>
    </section>

    <section class="panel panel--cover">
      <div class="brand">
        <span class="brand__mark"></span>
        <span class="brand__name">Bright JPR</span>
      </div>
      <h2 class="cover__headline">Caring for<br>Head Pain and<br>Sleep Apnea</h2>
      <p class="testimonial__quote">“I had TMJ pain for 15 years and spent a lot of time and money being treated for "TMJ" until Dr. Whitcombe correctly diagnosed that my pain was not from my joint, it was caused by muscles. I wish all doctors did as through an exam as Dr. Whitcombe. “</p>
      <p class="testimonial__author">Marissa, K. Los Angeles, California</p>
    </section>
  </main>
</body>
</html>
```